Real Estate Flyer (Brenton Property)

We need a color CMYK high resolution, print quality horizontal real estate property flyer designed in the sizes of 10" wide and 6.7425" tall and another one in 11" wide and 8.5" tall.
Ad should be professionally looking to U.S. standards. It should be sleek, modern yet classy.
We uploaded in Briefs logo files, agent photo, 2 photos of the property (Must use both) and a sample of a flyer for Vayle Morrow Luxury Residence. We like how the overlay atop the first photo in the Vayle Morrow flyer with the company logo in the overlay. We'd like to incorporate that with our logo, the background color of the overlay should match that of our logo. DON'T CHANGE LOGO COLORS. Only use two colors in ad (exact logo blue color and white). The text in the overlay must be "FOR SALE - Potential Income Producing Commercial Office Building". Other details that should be prominent underneath are "42 Brenton Dr., Schaumburg, IL 60174 - Asking Price: $650,000".
Add "Residential & Commercial" under our company logo in italic font.
Add in flyer: "Located seconds away from the Kettering Rd. & Palden Rd. Intersection"
Add in flyer:
- Completely vacant
- 10,000 sq. ft. building
- 55 Car Parking
- 1.38 acre lot
- Over 20 offices and 5 bathrooms.
- Lease out individual office spaces for great monthly cash flow
Put agent's photo and following details professionally displayed:
Dev Marlo
Managing Broker
847-555-0148
dev.marlo@qtnhomes-example.com
Add from Briefs fair housing logo and PLX logo near agent's information. Logos should be small but yet visible to understand text.
Add at bottom of the ad with separation near agent details:
Looking to Buy or Sell?
I’m your one-stop, full service licensed real estate broker.
I deal with all types of real estate properties: Homes, Condos, Townhomes, Multi-Unit Apartment Buildings and Commercial Spaces.
Let My Experience Guide You Through Every Step of the Process!
Fine print:
©2018 QTN Homes, Inc. All Rights Reserved.

```html
<!DOCTYPE html>
<html lang="en">
<head>
<meta charset="utf-8">
<title>Brenton Property – For Sale Flyer</title>
<link rel="stylesheet" href="https://fonts.googleapis.com/css2?family=Play:wght@400;700&family=PT+Sans:ital,wght@0,400;0,700;1,700&display=swap">
<style>
  :root{
    --brand-blue:#1d4fa4;
    --brand-blue-dark:#173f86;
    --white:#ffffff;
    --paper-light:#ffffff;
    --paper-shade:#e4e4e4;
    --ink:#1b1b1b;
    --stage:#e9e9e9;
  }
  *{margin:0;padding:0;box-sizing:border-box}
  html,body{width:1200px;height:1200px;overflow:hidden;background:var(--stage)}
  .flyer-frame{position:absolute;left:0;top:134px;width:1200px;height:931px;overflow:hidden}
  .flyer{position:absolute;left:0;top:0;width:1250px;height:970px;transform:scale(.96);transform-origin:0 0;
    background:linear-gradient(100deg,var(--paper-shade) 0%,var(--paper-light) 55%,var(--paper-light) 75%,#ececec 100%);
    font-family:"PT Sans",sans-serif;color:var(--ink)}
  .art{position:absolute;left:0;top:0;width:1250px;height:970px}
  .headline{position:absolute;right:38px;top:22px;width:800px;text-align:right;font-family:"Play",sans-serif;font-weight:700;
    font-size:33px;line-height:39px;color:var(--brand-blue);text-transform:uppercase;letter-spacing:.3px}
  .intro{position:absolute;left:668px;top:115px;width:550px;font-size:16.5px;line-height:21px;text-align:justify;text-align-last:right}
  .intro p+p{margin-top:21px}
  .info-title{position:absolute;right:32px;top:335px;font-family:"Play",sans-serif;font-weight:700;font-size:32px;color:var(--brand-blue)}
  .info-list{position:absolute;right:32px;top:383px;width:520px;list-style:none;text-align:right;font-size:20px;line-height:25px}
  .info-list li{margin-bottom:8px}
  .info-list li::before{content:"";display:inline-block;width:12px;height:10px;margin-right:10px;background:var(--brand-blue);
    clip-path:polygon(0 0,100% 50%,0 100%,25% 50%)}
  .overlay-text{position:absolute;left:278px;top:807px;width:290px;text-align:center;color:var(--white)}
  .overlay-text .sale{font-family:"Play",sans-serif;font-weight:700;font-size:17px;line-height:21px}
  .overlay-text .sale-sub{font-family:"Play",sans-serif;font-weight:700;font-size:18px;line-height:21px}
  .overlay-text .address{font-size:10px;margin-top:8px;white-space:nowrap}
  .brand{position:absolute;left:28px;top:812px;width:240px;color:var(--white);text-align:center}
  .brand-name{display:flex;align-items:center;justify-content:center;gap:10px;font-family:"Play",sans-serif;font-weight:700;font-size:34px;letter-spacing:1px;margin-top:10px}
  .brand-name .mark{width:16px;height:16px;background:var(--white)}
  .brand-tag{font-family:"PT Sans",sans-serif;font-style:italic;font-weight:700;font-size:17px;letter-spacing:.5px;margin-top:18px;text-transform:uppercase}
  .agent-label{position:absolute;left:610px;top:850px;width:244px;text-align:center;color:var(--white);font-family:"Play",sans-serif;font-weight:700}
  .agent-label .name{font-size:15px;line-height:18px;text-transform:uppercase}
  .agent-label .role{font-size:16px;line-height:20px}
  .contact{position:absolute;left:858px;top:710px;color:var(--white);font-family:"Play",sans-serif;font-weight:700;white-space:nowrap}
  .contact .cta{font-size:15px;line-height:20px}
  .contact .phone{font-size:24px;line-height:30px;margin-left:17px}
  .contact .email{font-size:18px;line-height:26px;margin-left:17px}
  .pitch{position:absolute;left:858px;top:809px;width:352px;text-align:center;font-size:10.5px;line-height:13px}
  .pitch h3{font-family:"Play",sans-serif;font-size:13.5px;color:var(--brand-blue);margin:0 0 1px -70px}
  .promise{position:absolute;left:860px;top:877px;color:var(--white);font-family:"Play",sans-serif;font-weight:700;font-size:15px;line-height:19px}
  .copyright{position:absolute;left:0;width:1286px;top:935px;text-align:center;font-size:13px}
</style>
</head>
<body>
<div class="flyer-frame">
  <div class="flyer">
    <svg class="art" viewBox="0 0 1250 970">
      <defs>
        <linearGradient id="facade" x1="0" y1="0" x2="0" y2="1">
          <stop offset="0" stop-color="#b9ab98"/>
          <stop offset=".55" stop-color="#8b7e70"/>
          <stop offset=".85" stop-color="#a0884a"/>
          <stop offset="1" stop-color="#7f9a45"/>
        </linearGradient>
        <linearGradient id="lot" x1="0" y1="0" x2="0" y2="1">
          <stop offset="0" stop-color="#c9d3de"/>
          <stop offset=".4" stop-color="#e8c79a"/>
          <stop offset=".55" stop-color="#6e6a62"/>
          <stop offset="1" stop-color="#2f3134"/>
        </linearGradient>
        <linearGradient id="portrait" x1="0" y1="0" x2="0" y2="1">
          <stop offset="0" stop-color="#ffffff"/>
          <stop offset="1" stop-color="#dcdcdc"/>
        </linearGradient>
      </defs>

      <polygon points="0,0 350,0 482,218 378,790 400,918 350,970 0,970" fill="url(#facade)" role="img" aria-label="Photo of the property entrance with arched doorway, number 202 and flower garden"/>
      <polyline points="350,0 482,218" fill="none" stroke="var(--brand-blue)" stroke-width="9"/>
      <polyline points="348,970 385,920" fill="none" stroke="var(--brand-blue)" stroke-width="9"/>

      <polygon points="0,791 568,791 600,855 568,920 0,920" fill="var(--brand-blue)"/>
      <line x1="278" y1="802" x2="278" y2="910" stroke="var(--white)" stroke-width="1.5"/>

      <polygon points="345,348 407,213 593,213 655,348 593,484 407,484" fill="var(--brand-blue)"/>
      <polygon points="361,348 416,225 584,225 639,348 584,472 416,472" fill="url(#lot)" role="img" aria-label="Photo of the office building at sunset across the parking lot"/>

      <polygon points="590,495 653,360 840,360 903,495 840,631 653,631" fill="var(--brand-blue)"/>
      <polygon points="606,495 662,372 831,372 887,495 831,619 662,619" fill="url(#lot)" role="img" aria-label="Photo of the parking lot with accessible parking spaces"/>

      <polygon points="345,631 407,500 593,500 655,631 593,762 407,762" fill="var(--brand-blue)"/>
      <polygon points="361,631 416,512 584,512 639,631 584,750 416,750" fill="url(#lot)" role="img" aria-label="Photo of the office building front with autumn tree and parked car"/>

      <polygon points="603,806 655,693 809,693 861,806 809,920 655,920" fill="var(--brand-blue)"/>
      <polygon points="617,806 663,705 801,705 847,806 801,908 663,908" fill="url(#portrait)" role="img" aria-label="Portrait photo of the managing broker"/>
      <polygon points="635,846 829,846 801,908 663,908" fill="var(--brand-blue-dark)"/>

      <polygon points="823,694 1163,694 1218,803 823,803" fill="var(--brand-blue)"/>
      <polygon points="823,873 1218,873 1163,921 823,921" fill="var(--brand-blue)"/>

      <rect x="1060" y="623" width="32" height="32" fill="var(--ink)" role="img" aria-label="Fair housing badge"/>
      <rect x="1123" y="620" width="90" height="40" fill="var(--white)" stroke="var(--ink)" stroke-width="1.5" role="img" aria-label="PLX listing service badge"/>
    </svg>

    <h1 class="headline">Located seconds away from the Kettering Rd. &amp; Palden Rd. Intersection</h1>

    <div class="intro">
      <p>Lorem ipsum dolor sit amet, consectetuer adipiscing elit. Aenean commodo ligula eget dolor. Aenean massa. Cum sociis natoque penatibus et magnis dis parturient montes, nascetur ridiculus mus. Donec quam felis, ultricies nec, pellentesque eu, pretium quis, sem. Nulla consequat massa quis enim. Donec pede justo, fringilla vel, aliquet nec, vulputate eget, arcu.</p>
      <p>Integer tincidunt. Cras dapibus. Vivamus elementum semper nisi. Aenean vulputate eleifend tellus. Aenean leo ligula, porttitor eu, consequat vitae, eleifend ac, enim.</p>
    </div>

    <h2 class="info-title">PROPERTY INFO</h2>
    <ul class="info-list">
      <li>Completely vacant</li>
      <li>10,000 sq. ft. building</li>
      <li>55 Car Parking</li>
      <li>1.38 acre lot</li>
      <li>Over 20 offices and 5 bathrooms.</li>
      <li>Lease out individual office spaces<br>for great monthly cash flow</li>
    </ul>

    <div class="brand">
      <div class="brand-name"><span class="mark"></span>QTN HOMES</div>
      <div class="brand-tag">Residential &amp; Commercial</div>
    </div>

    <div class="overlay-text">
      <div class="sale">FOR SALE</div>
      <div class="sale-sub">Potential Income Producing<br>Commercial Office Building</div>
      <div class="address">42 Brenton Dr., Schaumburg, IL 60174 - Asking Price: $650,000</div>
    </div>

    <div class="agent-label">
      <div class="name">Dev Marlo</div>
      <div class="role">Managing Broker</div>
    </div>

    <div class="contact">
      <div class="cta">CONTACT TODAY !</div>
      <div class="phone">847-555-0148</div>
      <div class="email">dev.marlo@qtnhomes-example.com</div>
    </div>

    <div class="pitch">
      <h3>Looking to Buy or Sell?</h3>
      <p>I’m your one-stop, full service licensed real estate broker. I deal with all types of real estate properties: Homes, Condos, Townhomes, Multi-Unit Apartment Buildings and Commercial Spaces.</p>
    </div>

    <div class="promise">Let My Experience Guide You Through Every<br>Step of the Process!</div>

    <p class="copyright">©2018 QTN Homes, Inc. All Rights Reserved.</p>
  </div>
</div>
</body>
</html>
```